Painting Valtoni Renovations New buildings

Paint jobs plasterwork renovations new building customer painter paper drywall Entsorgungen.neukunden win color splash pleasure in colors competent clean fast reliable new try build demolition color combinations color concepts offers washing façade painting wood stains new projects old building renovations yes no beautiful new old sell secure solve paint over paint paint spray paint lye assemble disassemble sell buy trade oil dust new old assembly disassembly putty sanding fashion devastation copying belief feng shui kleopatra pompes beer colors swamp lime abrasion release tighten

Target Market(s)

construction industry

Contact Information for Business Card

Maler

Font styles to use
Serif

Colors
f04a50
959595

Requirements
Must have
• elegant appearance
Nice to have
• simply goal-oriented clientele in detail
Should not have
• too colorful

```html
<!DOCTYPE html>
<html lang="en">
<head>
<meta charset="utf-8">
<title>Valtoni Malerbetrieb – Business Card</title>
<link rel="stylesheet" href="https://fonts.googleapis.com/css2?family=Lato:wght@400;700&display=swap">
<style>
  :root {
    --backdrop: #1c1c1c;
    --card: #111111;
    --brand-blue: #2b4c93;
    --brand-grey: #9a9a9a;
    --accent: #f4b122;
    --ink: #e6e6e6;
    --rule: #4a4a4a;
  }
  * { margin: 0; padding: 0; box-sizing: border-box; }
  html, body {
    width: 1200px; height: 900px; overflow: hidden;
    background: var(--backdrop);
    font-family: "Lato", Arial, sans-serif;
  }
  .stage {
    position: relative; width: 1200px; height: 900px;
  }
  .card {
    position: absolute; left: 320px; width: 560px; height: 320px;
    background: var(--card); border-radius: 22px;
    box-shadow: 0 14px 30px rgba(0,0,0,.55);
  }
  .card--back { top: 90px; }
  .card--front { top: 490px; }

  .wordmark {
    position: absolute; font-weight: 700; letter-spacing: .5px;
    display: flex; align-items: center; gap: 10px;
  }
  .wordmark__dot { width: 14px; height: 14px; border-radius: 50%; }
  .wordmark__name { font-size: 40px; line-height: 1; }
  .wordmark__sub { font-size: 13px; display: block; margin-top: 4px; letter-spacing: 1px; }

  .card--back .wordmark {
    left: 0; right: 0; top: 118px; justify-content: center; color: var(--brand-grey);
  }
  .card--back .wordmark__dot { background: var(--brand-grey); }

  .card--front .wordmark { right: 36px; top: 44px; color: var(--brand-blue); }
  .card--front .wordmark__dot { background: var(--brand-blue); }

  .divider {
    position: absolute; left: 230px; right: 36px; top: 150px;
    height: 1px; background: var(--rule);
  }
  .address {
    position: absolute; right: 36px; top: 168px; text-align: right;
    color: var(--ink); font-size: 15px; line-height: 1.4;
  }
  .person { position: absolute; left: 36px; top: 150px; }
  .person__name { color: var(--accent); font-size: 24px; font-weight: 700; font-style: italic; }
  .person__role { color: var(--ink); font-size: 15px; margin-top: 2px; }
  .contacts { position: absolute; left: 48px; top: 228px; list-style: none; }
  .contacts li {
    display: flex; align-items: center; gap: 8px;
    color: var(--ink); font-size: 15px; line-height: 23px;
  }
  .contacts svg { width: 13px; height: 13px; fill: var(--accent); flex: none; }
</style>
</head>
<body>
<main class="stage">
  <section class="card card--back" aria-label="Card back">
    <div class="wordmark">
      <span class="wordmark__dot"></span>
      <span><span class="wordmark__name">Valtoni</span><span class="wordmark__sub">Malerbetrieb</span></span>
    </div>
  </section>

  <section class="card card--front" aria-label="Card front">
    <div class="wordmark">
      <span class="wordmark__dot"></span>
      <span><span class="wordmark__name">Valtoni</span><span class="wordmark__sub">Malerbetrieb</span></span>
    </div>
    <div class="divider"></div>
    <address class="address" style="font-style:normal">18 Farbgasse<br>Zurich, 8004</address>
    <div class="person">
      <p class="person__name">Merenda Valtoni</p>
      <p class="person__role">Managing Director</p>
    </div>
    <ul class="contacts">
      <li><svg viewBox="0 0 16 16" aria-hidden="true"><path d="M3 1h3l1.5 4-2 1.3a9 9 0 0 0 4.2 4.2L11 8.5l4 1.5v3c0 1-1 2-2 2A12 12 0 0 1 1 3c0-1 1-2 2-2z"/></svg>044-210 384 615</li>
      <li><svg viewBox="0 0 16 16" aria-hidden="true"><path d="M1 3h14v10H1z M1 3l7 6 7-6" stroke="#111" stroke-width="1.2"/></svg>info@valtoni-maler.com</li>
      <li><svg viewBox="0 0 16 16" aria-hidden="true"><circle cx="8" cy="8" r="7"/><path d="M1 8h14M8 1c3 3 3 11 0 14M8 1c-3 3-3 11 0 14" stroke="#111" stroke-width="1.1" fill="none"/></svg>www.valtoni-maler.com</li>
    </ul>
  </section>
</main>
</body>
</html>
```